New startup requiring business card

New company needed a business card / logo. Company name is
Minthel
Company is providing IT software sales, partnering and consulting services across the APAC region. Catch line is "stronger as one".
We currently have a feeling yellow as the primary colour given its meaning across the region but open to ideas. Main brief is we want something smart, clean and professional while still leveraging the strength of the name.
A major part of the business is mutually beneficial partnerships, not sure if this helps but maybe visual around linkages between objects.
Also wanting a standard size card, preference is something that will have a D/S cello sheen finish in a matt. But again open to ideas, wow us!
Software

```html
<!DOCTYPE html>
<html lang="en">
<head>
<meta charset="utf-8">
<title>Minthel — Business Card</title>
<link rel="stylesheet" href="https://fonts.googleapis.com/css2?family=Didact+Gothic&display=swap">
<style>
  :root {
    --stage: #2a2a2a;
    --card-light: #f8ee2c;
    --card-dark: #dcd014;
    --ink: #111111;
    --ink-soft: #2b2b1a;
  }
  * { margin: 0; padding: 0; box-sizing: border-box; }
  html, body {
    width: 1200px; height: 900px; overflow: hidden;
    background: var(--stage);
    font-family: "Didact Gothic", "Century Gothic", sans-serif;
    color: var(--ink);
  }
  .stage { position: relative; width: 1200px; height: 900px; }
  .card {
    position: absolute;
    width: 620px; height: 354px;
    border-radius: 20px;
    background: linear-gradient(135deg, var(--card-light) 0%, var(--card-light) 45%, var(--card-dark) 100%);
  }
  .card--front { left: 80px; top: 70px; }
  .card--back { left: 500px; top: 476px; }

  .brand { position: absolute; display: flex; flex-direction: column; align-items: flex-start; }
  .brand__row { display: flex; align-items: center; gap: 10px; }
  .brand__dot { width: 28px; height: 28px; border-radius: 50%; background: var(--ink); }
  .brand__name { font-size: 46px; line-height: 1; letter-spacing: 1px; color: var(--ink); }
  .brand__tagline {
    align-self: stretch;
    font-size: 11px; letter-spacing: 3px; text-transform: uppercase;
    margin-top: 8px; padding-top: 6px;
    border-top: 1px solid var(--ink);
    color: var(--ink);
    text-align: center;
  }

  .card--front .brand { left: 50%; top: 50%; transform: translate(-50%, -50%); }
  .card--back .brand { left: 52px; top: 58px; }
  .card--back .brand__name { font-size: 40px; }
  .card--back .brand__dot { width: 24px; height: 24px; }
  .card--back .brand__tagline { font-size: 10px; letter-spacing: 2.5px; }

  .person { position: absolute; right: 56px; top: 74px; display: flex; gap: 10px; }
  .person__bar { width: 4px; height: 34px; background: var(--ink); }
  .person__name { font-size: 21px; line-height: 1.05; }
  .person__role { font-size: 10px; color: var(--ink-soft); }

  .contacts {
    position: absolute; left: 52px; right: 56px; bottom: 46px;
    display: flex; justify-content: space-between; align-items: center;
    font-size: 14px; color: var(--ink-soft);
  }
  .contact { display: flex; align-items: center; gap: 8px; }
  .contact svg { width: 14px; height: 14px; fill: none; stroke: var(--ink-soft); stroke-width: 1.2; }
</style>
</head>
<body>
<main class="stage">
  <section class="card card--front" aria-label="Card front">
    <div class="brand">
      <div class="brand__row">
        <span class="brand__dot"></span>
        <span class="brand__name">minthel</span>
      </div>
      <span class="brand__tagline">stronger as one</span>
    </div>
  </section>

  <section class="card card--back" aria-label="Card back">
    <div class="brand">
      <div class="brand__row">
        <span class="brand__dot"></span>
        <span class="brand__name">minthel</span>
      </div>
      <span class="brand__tagline">stronger as one</span>
    </div>

    <div class="person">
      <span class="person__bar"></span>
      <div>
        <p class="person__name">Daniel Reyes</p>
        <p class="person__role">general manager</p>
      </div>
    </div>

    <div class="contacts">
      <p class="contact">
        <svg viewBox="0 0 14 14" aria-hidden="true"><rect x="3.5" y="1" width="7" height="12" rx="1.2"/><line x1="6" y1="11" x2="8" y2="11"/></svg>
        012 4848 5151 60
      </p>
      <p class="contact">
        <svg viewBox="0 0 14 14" aria-hidden="true"><rect x="1" y="3" width="12" height="8"/><polyline points="1,3 7,8 13,3"/></svg>
        reyes@minthel.com
      </p>
      <p class="contact">
        <svg viewBox="0 0 14 14" aria-hidden="true"><polyline points="1,7 7,1.5 13,7"/><polyline points="3,6 3,12.5 11,12.5 11,6"/></svg>
        www.minthel.com
      </p>
    </div>
  </section>
</main>
</body>
</html>
```